VALMIKE GROUP

This is a company that provides executive protection. Our motto is "New Era in Protection"... I don't want this to look like other security websites. I want it to be clean and sharp and represent a new era. We are based in the bay area so maybe a picture of San Francisco in the background?
I want it to be able to funnel down a couple different categories.
1. About Us
2. Services (Executive Protection, Covert Protection, Residential Protection & Intelligence)
3. Iron Finch (Training & Consulting)
4. Contact Us
I want it to be very clean and modern. I don't want there to be any pictures of bodyguards with ear pieces like every other website.
Target Market(s)
Ultra High Net Worth Individuals
Coding
Coded - Design and coding required
Number of Pages Required
1 page
Requirements
Must have
- Colors of my Symbol
Nice to have
- City in the background, San Francisco, New York or the Pinehallow Club in Montana.
Should not have
- Should not look like an KVM website or have photos of bodyguards. I want this to be a clean and simple website with my logo

```html
<!DOCTYPE html>
<html lang="en">
<head>
<meta charset="utf-8">
<title>Valmike Group — A New Era in Protection</title>
<link rel="stylesheet" href="https://fonts.googleapis.com/css2?family=Michroma&family=Lato:wght@400;700;900&display=swap">
<style>
:root{
  --red:#a3171e;
  --red-deep:#7d1015;
  --red-bar:#8c1319;
  --ink:#1d1d1f;
  --white:#ffffff;
  --mist:#f2f2f2;
  --grey:#6b6b6b;
}
*{box-sizing:border-box;margin:0;padding:0}
html,body{width:687px;height:1200px;overflow:hidden}
body{position:relative;background:var(--white);font-family:"Lato",Arial,sans-serif;color:var(--ink)}
a{text-decoration:none}
.abs{position:absolute}
.wide{font-family:"Michroma",sans-serif;letter-spacing:1px}

/* top bar */
.topbar{top:0;left:0;width:687px;height:20px;background:var(--red-bar);color:var(--white);font-size:8px;display:flex;align-items:center;justify-content:space-between;padding:0 92px}
.social{display:flex;gap:8px}
.social span{width:7px;height:7px;border-radius:50%;background:var(--white);opacity:.9;display:block}
.contact-mini{display:flex;gap:22px;align-items:center}
.contact-mini span{display:flex;gap:4px;align-items:center}

/* header */
.header{top:20px;left:0;width:687px;height:50px;background:var(--white);display:flex;align-items:center;justify-content:space-between;padding:0 92px}
.brand{display:flex;align-items:center;gap:7px;font-family:"Michroma",sans-serif;font-size:13px;color:var(--ink);letter-spacing:1px;line-height:1}
.brand i{width:20px;height:20px;background:var(--red);display:block}
.brand small{display:block;font-size:6px;letter-spacing:4px;margin-top:2px}
.nav{display:flex;gap:20px;font-size:9px;font-weight:700}
.nav a{color:var(--ink);padding-bottom:3px}
.nav a.active{border-bottom:2px solid var(--red)}

/* hero */
.hero-photo{top:70px;left:0;width:687px;height:300px;background:linear-gradient(180deg,#7d8aa3 0%,#a89a93 35%,#8d6b5d 60%,#3b3538 100%)}
.hero-title{top:168px;left:0;width:687px;text-align:center;color:var(--white);font-size:24px;font-weight:400;line-height:1.35;text-shadow:0 2px 6px rgba(0,0,0,.4)}
.btn{background:var(--red);color:var(--white);font-size:9px;font-weight:900;letter-spacing:1px;padding:7px 12px;display:inline-block}
.hero-btn{top:257px;left:286px}

/* services */
.services-bg{top:0;left:0}
.section-kicker{color:var(--red);font-size:13px;font-weight:900;letter-spacing:2px;text-align:center}
.section-title{font-size:24px;font-weight:400;text-align:center;color:var(--ink)}
.services-head{top:415px;left:0;width:687px}
.service{width:110px;text-align:center}
.service p{font-size:9px;font-weight:900;line-height:1.3;margin-top:10px;text-transform:uppercase}

/* about */
.about-text{top:770px;left:322px;width:330px;color:var(--white)}
.about-text .kicker{font-size:14px;font-weight:900;letter-spacing:2px}
.about-text h2{font-family:"Michroma",sans-serif;font-size:22px;letter-spacing:1px;font-weight:400;line-height:1.1}
.about-text h2 small{font-size:9px;letter-spacing:5px}
.about-text .lead{font-size:9.5px;font-weight:700;line-height:1.5;margin-top:10px}
.about-text .body{font-size:8.5px;line-height:1.6;margin-top:10px;opacity:.85}
.about-text .btn{margin-top:16px;background:var(--white);color:var(--ink)}

/* footer */
.footer{top:1030px;left:0;width:687px;height:155px;background:var(--red)}
.footer .brand{position:absolute;left:92px;top:34px;color:var(--white)}
.footer .brand i{background:var(--white)}
.foot-contact{position:absolute;top:40px;left:352px;display:flex;gap:30px;color:var(--white);font-size:8px}
.foot-contact span{display:flex;align-items:center;gap:7px}
.ico-box{width:18px;height:18px;background:var(--white);display:flex;align-items:center;justify-content:center}
.foot-nav{position:absolute;top:99px;left:92px;display:flex;gap:4px}
.foot-nav a{font-size:8px;color:var(--white);border:1px solid rgba(255,255,255,.35);padding:6px 13px;background:rgba(0,0,0,.08)}
.foot-nav a.sq{width:30px;padding:6px 0;display:flex;justify-content:center;align-items:center}
.foot-nav a.sq span{width:7px;height:7px;border-radius:50%;background:var(--white);display:block}
.copyright{top:1185px;left:0;width:687px;height:15px;background:var(--red-deep);color:var(--white);font-size:7px;display:flex;align-items:center;justify-content:space-between;padding:0 92px}
</style>
</head>
<body>

<div class="abs topbar">
  <div class="social" aria-label="Social links"><span></span><span></span><span></span><span></span></div>
  <div class="contact-mini">
    <span><svg width="7" height="7" viewBox="0 0 10 10"><path d="M2 0l2 2-1 2a6 6 0 003 3l2-1 2 2-2 2A9 9 0 010 2z" fill="#fff"/></svg>+415 555 0142</span>
    <span><svg width="8" height="6" viewBox="0 0 10 8"><rect width="10" height="8" fill="#fff"/><path d="M0 0l5 4 5-4" stroke="#8c1319" fill="none"/></svg>info@valmikegroup.com</span>
  </div>
</div>

<header class="abs header">
  <div class="brand"><i></i><div>VALMIKE<small>GROUP</small></div></div>
  <nav class="nav"><a class="active" href="#">Home</a><a href="#">About Us</a><a href="#">Services</a><a href="#">Iron Finch</a><a href="#">Contact Us</a></nav>
</header>

<div class="abs hero-photo" role="img" aria-label="San Francisco skyline at dusk with tower and mountain"></div>
<h1 class="abs hero-title wide">DEFINING A NEW ERA<br>IN PROTECTION</h1>
<a class="abs btn hero-btn" href="#">CONTACT US</a>

<svg class="abs services-bg" width="687" height="720" viewBox="0 0 687 720">
  <polygon points="0,350 150,330 300,362 687,300 687,660 380,645 0,700" fill="#ffffff"/>
  <polyline points="150,330 300,362 460,336" fill="none" stroke="#a3171e" stroke-width="3"/>
</svg>
<div class="abs" role="img" aria-label="Golden Gate Bridge over the bay" style="top:290px;left:565px;width:122px;height:400px;background:linear-gradient(180deg,#f4f4f6 0%,#d9d3cf 40%,#b3726a 65%,#6f5a57 100%);clip-path:polygon(35% 10%,100% 0,100% 100%,0 90%,20% 45%)"></div>

<div class="abs services-head">
  <p class="section-kicker">SERVICES</p>
  <h2 class="section-title wide">WHAT WE OFFER</h2>
</div>

<div class="abs service" style="top:482px;left:117px">
  <svg width="46" height="52" viewBox="0 0 46 52"><path d="M2 2h42v34L23 50 2 36z" fill="#fff" stroke="#a3171e" stroke-width="3"/><circle cx="17" cy="18" r="4" fill="#1d1d1f"/><circle cx="29" cy="18" r="4" fill="#1d1d1f"/><rect x="11" y="24" width="11" height="8" rx="3" fill="#a3171e"/><rect x="24" y="24" width="11" height="8" rx="3" fill="#a3171e"/></svg>
  <p>Executive<br>Protection</p>
</div>
<div class="abs service" style="top:480px;left:290px">
  <svg width="46" height="52" viewBox="0 0 46 52"><path d="M2 2h42v34L23 50 2 36z" fill="#fff" stroke="#a3171e" stroke-width="3"/><path d="M11 23l12-9 12 9" fill="none" stroke="#a3171e" stroke-width="3"/><rect x="15" y="23" width="16" height="10" fill="#1d1d1f"/></svg>
  <p>Residential<br>Protection</p>
</div>
<div class="abs service" style="top:482px;left:445px">
  <svg width="46" height="52" viewBox="0 0 46 52"><path d="M2 2h42v34L23 50 2 36z" fill="#fff" stroke="#a3171e" stroke-width="3"/><circle cx="17" cy="18" r="4" fill="#1d1d1f"/><circle cx="29" cy="18" r="4" fill="#1d1d1f"/><rect x="11" y="24" width="11" height="8" rx="3" fill="#1d1d1f"/><rect x="24" y="24" width="11" height="8" rx="3" fill="#a3171e"/></svg>
  <p>Covert<br>Protection</p>
</div>

<div class="abs" role="img" aria-label="Dark city skyline with red overlay" style="top:650px;left:0;width:687px;height:380px;background:linear-gradient(160deg,#6b2226 0%,#3a2b2e 45%,#262427 100%);clip-path:polygon(0 13%,380px 0,100% 4%,100% 100%,0 100%)"></div>
<svg class="abs" style="top:650px;left:0" width="687" height="60" viewBox="0 0 687 60"><polyline points="0,50 380,0 687,12" fill="none" stroke="#a3171e" stroke-width="3"/></svg>
<div class="abs" style="top:770px;left:60px;width:160px;height:190px;background:rgba(163,23,30,.35)" role="img" aria-label="Faint red brand panel"></div>

<div class="abs about-text">
  <p class="kicker">ABOUT</p>
  <h2>VALMIKE <small>GROUP</small></h2>
  <p class="lead">Trusted protection for principals, families and estates across the bay area and beyond, delivered with calm discretion.</p>
  <p class="body">Our team blends field experience with modern intelligence to plan every movement, secure every residence and keep daily life running smoothly. We stay quiet, prepared and precise.</p>
  <a class="btn" href="#">READ MORE</a>
</div>

<footer class="abs footer">
  <div class="brand"><i></i><div>VALMIKE<small>GROUP</small></div></div>
  <div class="foot-contact">
    <span><i class="ico-box"><svg width="9" height="9" viewBox="0 0 10 10"><path d="M2 0l2 2-1 2a6 6 0 003 3l2-1 2 2-2 2A9 9 0 010 2z" fill="#a3171e"/></svg></i>+415 555 0142</span>
    <span><i class="ico-box"><svg width="10" height="8" viewBox="0 0 10 8"><rect width="10" height="8" fill="#a3171e"/><path d="M0 0l5 4 5-4" stroke="#fff" fill="none"/></svg></i>info@valmikegroup.com</span>
  </div>
  <nav class="foot-nav">
    <a href="#">Home</a><a href="#">About Us</a><a href="#">Services</a><a href="#">Iron Finch</a><a href="#">Contact Us</a>
    <a class="sq" href="#" aria-label="Social"><span></span></a><a class="sq" href="#" aria-label="Social"><span></span></a><a class="sq" href="#" aria-label="Social"><span></span></a><a class="sq" href="#" aria-label="Social"><span></span></a>
  </nav>
</footer>
<div class="abs copyright"><span>Copyright © 2021 Valmike Group. All Rights Reserved.</span><span>Privacy Policy</span></div>

</body>
</html>
```